Protein Powder Bag Design

We need a packaging design for a protein powder for our supplement company. The company is "Dawn Hollow" and the product is called "SUMMIT PROTEIN"

The bag design needs to include:

- Our Logo
- Grass-Fed Beef Isolate Powder
- Chocolate (as the flavor)
- 2lbs 900grams Dietary Supplement
- Matte finish

The back of the bag needs to include:

- Blurb about Dawn Hollow
i.e. Live Dawn Hollow for anything and part of that means dialing in your nutrition. We are about clean, real, whole foods, quality, transparency, health, performance, flexible lifestyle, convenience, paleo friendly, no gluten

- Supplement Facts (attached)
*Under Supplement Facts*
INGREDIENTS: Grass-Fed Beef Protein (CattlePRO TM), Cocoa Powder, Stevia Leaf Powder

- Barcode (attached)
- #eatrealfood
- info@dawnhollowfoods.example
- dawnhollowfoods.example
- Manufactured for Dawn Hollow, San Francisco, Ca 94107
- Collagen/Gellatin
- Complete source of protein
- Free from: dairy, gluten, whey, soy, antibiotics, hormones, fillers, artificial sweeteners, preservatives, and other nonsense.

- Suggested Use:
Mix with 8 to 10 oz of liquid or add to baked foods to feel amazing. Store in a dry, cool place.

- Ingredients Per Scoop:
4 oz grass-fed beef
Cocoa Powder
Stevia

- **These statements have not been evaluated by The Board of Nutrient Oversight. This product is not intended to diagnose, treat, cure or prevent disease.

• - Matte finish
• - Blue, white, color scheme
• - Check out the templates (do not copy)

```html
<!DOCTYPE html>
<html lang="en">
<head>
<meta charset="utf-8">
<title>Summit Protein – Pouch Front</title>
<link href="https://fonts.googleapis.com/css2?family=Oswald:wght@300;400;500&family=Fjalla+One&display=swap" rel="stylesheet">
<style>
  :root {
    --page: #ffffff;
    --pouch-green: #7fc743;
    --pouch-green-light: #93d35a;
    --band-blue: #2f93d6;
    --band-blue-deep: #1f7fc4;
    --cocoa: #3a2620;
    --cocoa-soft: #6b4d40;
    --ink-white: #f4f6f8;
    --rule: rgba(255,255,255,0.55);
  }
  * { margin: 0; padding: 0; box-sizing: border-box; }
  html, body {
    width: 1200px; height: 1200px; overflow: hidden;
    background: var(--page);
  }
  .canvas {
    position: relative; width: 1200px; height: 1200px;
  }
  .pouch {
    position: absolute; left: 290px; top: 170px;
    width: 620px; height: 860px;
    background: linear-gradient(180deg, var(--pouch-green-light), var(--pouch-green));
    border-radius: 10px 10px 14px 14px;
    overflow: hidden;
  }
  .pouch__seal {
    position: absolute; left: 30px; right: 30px; top: 80px;
    height: 8px;
    border-top: 2px solid rgba(0,0,0,0.08);
    border-bottom: 2px solid rgba(255,255,255,0.25);
  }
  .brand {
    position: absolute; left: 0; right: 0; top: 135px;
    display: flex; flex-direction: column; align-items: center; gap: 14px;
  }
  .brand__mark {
    width: 46px; height: 46px; background: var(--ink-white);
  }
  .brand__name {
    font-family: "Oswald", sans-serif; font-weight: 300;
    font-size: 26px; letter-spacing: 10px; color: var(--ink-white);
    text-transform: uppercase;
  }
  .band {
    position: absolute; left: 0; right: 0; top: 250px; height: 415px;
    background: var(--band-blue);
    border-top: 6px solid var(--cocoa);
  }
  .band__art {
    position: absolute; right: 0; top: 0; width: 330px; height: 409px;
    background: radial-gradient(ellipse at 75% 15%, #8a6a58 0%, #6b4d40 28%, var(--band-blue-deep) 60%, var(--band-blue) 85%);
  }
  .title {
    position: absolute; left: 72px; top: 48px;
    font-family: "Fjalla One", sans-serif; font-weight: 400;
    font-size: 84px; line-height: 0.98; color: var(--ink-white);
    letter-spacing: -1px;
  }
  .descriptor {
    position: absolute; left: 68px; top: 228px; width: 210px;
    padding: 10px 0 10px 6px;
    border-top: 1.5px solid var(--rule); border-bottom: 1.5px solid var(--rule);
    font-family: "Oswald", sans-serif; font-weight: 300;
    font-size: 31px; line-height: 1.05; color: var(--ink-white);
    text-transform: uppercase;
  }
  .flavor {
    position: absolute; right: 32px; top: 275px;
    width: 150px; height: 150px; border-radius: 50%;
    background: var(--cocoa-soft);
    display: flex; flex-direction: column; align-items: center; justify-content: center;
    color: var(--ink-white); font-family: "Oswald", sans-serif;
  }
  .flavor::before {
    content: ""; position: absolute; left: 30px; top: -18px;
    border-left: 14px solid transparent; border-right: 14px solid transparent;
    border-bottom: 30px solid var(--cocoa-soft); transform: rotate(-20deg);
  }
  .flavor__label { font-weight: 300; font-size: 22px; line-height: 1; }
  .flavor__name { font-weight: 400; font-size: 34px; line-height: 1.1; }
  .footer-band {
    position: absolute; left: 0; right: 0; top: 665px; height: 70px;
    background: linear-gradient(90deg, var(--cocoa), var(--cocoa-soft));
    display: flex; align-items: center; justify-content: center; gap: 10px;
    color: var(--ink-white); font-family: "Oswald", sans-serif;
  }
  .footer-band__weight { font-weight: 500; font-size: 23px; letter-spacing: 1px; }
  .footer-band__type { font-weight: 400; font-size: 15px; letter-spacing: 1px; padding-top: 4px; }
</style>
</head>
<body>
<main class="canvas">
  <section class="pouch">
    <div class="pouch__seal"></div>
    <header class="brand">
      <span class="brand__mark"></span>
      <span class="brand__name">Dawn Hollow</span>
    </header>
    <div class="band">
      <div class="band__art" role="img" aria-label="Chocolate pieces and cocoa powder with a white line drawing of a cow's head"></div>
      <h1 class="title">SUMMIT<br>PROTEIN</h1>
      <p class="descriptor">Grass-Fed<br>Beef<br>Isolate<br>Powder</p>
      <div class="flavor">
        <span class="flavor__label">flavor</span>
        <span class="flavor__name">Chocolate</span>
      </div>
    </div>
    <div class="footer-band">
      <span class="footer-band__weight">2LBS 900GRAMS</span>
      <span class="footer-band__type">DIETARY SUPPLEMENT</span>
    </div>
  </section>
</main>
</body>
</html>
```